Security Warning Sign

We have an existing sign that needs an update. I have attached a picture of the current square sign. We need to maintain the same wording. It needs to be professional and appropriate to attach to our customers fence. Also attached is a copy of our building sign which may lend some inspiration and hopefully the ai format will assist. The final sign will be 600mm x 600mmOur website is www.harbourlinewatch.com.au

```html
<!DOCTYPE html>
<html lang="en">
<head>
<meta charset="utf-8">
<title>Harbourline Watch – Surveillance Warning Sign</title>
<link rel="stylesheet" href="https://fonts.googleapis.com/css2?family=Montserrat:wght@700;800&family=Open+Sans:wght@700;800&display=swap">
<style>
  :root {
    --backdrop: #cfcfcf;
    --paper: #ffffff;
    --ink-dark: #242424;
    --ink-dark-2: #2d2d2d;
    --accent: #f58220;
    --stripe-grey: #4a4a4a;
    --text-light: #ffffff;
  }
  html, body {
    margin: 0;
    padding: 0;
    width: 1200px;
    height: 1200px;
    overflow: hidden;
    background: var(--backdrop);
  }
  .canvas {
    position: relative;
    width: 1200px;
    height: 1200px;
  }
  .sign {
    position: absolute;
    left: 88px;
    top: 88px;
    width: 1025px;
    height: 1024px;
    background: var(--ink-dark);
    box-shadow: 4px 6px 10px rgba(0,0,0,0.35);
    overflow: hidden;
  }
  .sign-header {
    position: absolute;
    left: 0; top: 0;
    width: 100%;
    height: 217px;
    background: var(--paper);
    display: flex;
    align-items: center;
    justify-content: center;
  }
  .sign-title {
    margin: 0;
    font-family: "Montserrat", sans-serif;
    font-weight: 700;
    font-size: 150px;
    letter-spacing: 0;
    line-height: 1;
    color: var(--accent);
    transform: translateY(4px);
  }
  .sign-body {
    position: absolute;
    left: 0; top: 217px;
    width: 100%;
    height: 807px;
    background: linear-gradient(150deg, var(--ink-dark-2) 0%, var(--ink-dark) 45%, #1f1f1f 70%, var(--ink-dark-2) 100%);
  }
  .notice {
    position: absolute;
    left: 0;
    top: 54px;
    width: 100%;
    margin: 0;
    text-align: center;
    font-family: "Montserrat", sans-serif;
    font-weight: 700;
    font-size: 74px;
    line-height: 101px;
    letter-spacing: 2px;
    color: var(--text-light);
  }
  .brand {
    position: absolute;
    left: 60px;
    top: 680px;
    display: flex;
    align-items: center;
    gap: 22px;
  }
  .brand-dot {
    width: 90px;
    height: 90px;
    border-radius: 50%;
    background: var(--accent);
  }
  .brand-name {
    font-family: "Montserrat", sans-serif;
    font-weight: 700;
    font-size: 92px;
    line-height: 1;
    color: var(--text-light);
  }
  .company {
    position: absolute;
    right: 66px;
    top: 634px;
    margin: 0;
    font-family: "Montserrat", sans-serif;
    font-weight: 700;
    font-size: 29px;
    letter-spacing: 1.5px;
    color: var(--text-light);
  }
  .contact-band {
    position: absolute;
    left: 430px;
    top: 686px;
    width: 595px;
    height: 80px;
  }
  .band-shape { position: absolute; left: 0; top: 0; }
  .phone {
    position: absolute;
    left: 112px;
    top: 0;
    height: 80px;
    display: flex;
    align-items: center;
    gap: 16px;
    font-family: "Open Sans", sans-serif;
    font-weight: 800;
    font-size: 54px;
    color: var(--text-light);
  }
  .phone-icon { flex: none; display: block; }
</style>
</head>
<body>
<div class="canvas">
  <div class="sign">
    <header class="sign-header">
      <h1 class="sign-title">WARNING</h1>
    </header>
    <section class="sign-body" role="img" aria-label="Dark charcoal faceted geometric background">
      <p class="notice">ELECTRONIC<br>SURVEILLANCE<br>AND RECORDING<br>DEVICES INSTALLED<br>IN THIS AREA</p>

      <div class="brand">
        <span class="brand-dot"></span>
        <span class="brand-name">HLW</span>
      </div>

      <p class="company">HARBOURLINE WATCH</p>

      <div class="contact-band">
        <svg class="band-shape" width="595" height="80" viewBox="0 0 595 80" aria-hidden="true">
          <polygon points="52,0 66,0 18,80 4,80" fill="var(--stripe-grey)"/>
          <polygon points="82,0 595,0 595,80 34,80" fill="var(--accent)"/>
        </svg>
        <div class="phone">
          <svg class="phone-icon" width="50" height="50" viewBox="0 0 24 24" aria-hidden="true">
            <path fill="#ffffff" d="M6.6 10.8c1.4 2.8 3.8 5.1 6.6 6.6l2.2-2.2c.3-.3.7-.4 1-.2 1.1.4 2.3.6 3.6.6.6 0 1 .4 1 1V20c0 .6-.4 1-1 1C10.6 21 3 13.4 3 4c0-.6.4-1 1-1h3.5c.6 0 1 .4 1 1 0 1.3.2 2.5.6 3.6.1.3 0 .7-.2 1L6.6 10.8z"/>
            <path fill="none" stroke="#ffffff" stroke-width="1.6" stroke-linecap="round" d="M14 3.5a7 7 0 0 1 6.5 6.5M14 7a3.6 3.6 0 0 1 3 3"/>
          </svg>
          <span>1300 555 017</span>
        </div>
      </div>
    </section>
  </div>
</div>
</body>
</html>
```